Inspiring Poster for Company Staff Room

What we need:
We want an awesome design to create a poster that will be plaque mounted in our staff room. We just went through a very motivating workshop to discover our "WHY" as a company...basically, to define the reason we are in business, and to define what motivates us to come to work every day. The poster must be motivating but really resonate with our team…we are not looking for a “typical” motivational poster that we can purchase off Brindleway!

Who we are:
We are a property management company, a team of 20 that is passionate about our investors, and residents who rent from us, but more importantly, we love helping people and making a difference in our industry. We are proud and work hard for every single 5 star Quorvix review we achieve.

Information for you:
We have included a mock up of the poster, which words we want, and the placement of them (in a general sense) but we need a designer to really bring this together in an inspiring poster that represents our company’s culture, feel, and fit. We have also included a logo file, as well as examples of our business cards, letterhead and thank you card already designed.
Here are the parameters:

(1) Poster size: 24” x 36”
(2) Full colour
(3) Must incorporate our company logo
(4) Must incorporate the following words:

Why do I come to work?

“To feel fulfilled by empathizing, educating and empowering our clients and co-workers so that we can build strong, impactful relationships”

Own the outcome

(5) Please see our website at www.larkmoorpm.example to get a feel for our company culture and for a better idea of our current company graphics

Target Market(s)

Our staff. Will not be seen by our clients

Industry/Entity Type

Real Estate

Font styles to use
Serif
Sans Serif

Requirements
Should not have
• Would not want this to be too "busy." if you can picture it, the poster will be mounted on the wall as soon as someone enters the room. The idea is to remind them each day why they come to work.

```html
<!DOCTYPE html>
<html lang="en">
<head>
<meta charset="utf-8">
<title>Larkmoor Property Management – Why Do I Come to Work?</title>
<link rel="stylesheet" href="https://fonts.googleapis.com/css2?family=Archivo:ital,wdth,wght@0,62..125,400..900;1,62..125,400..900&display=swap">
<style>
  :root {
    --brand-blue: #0e8fcc;
    --charcoal: #2f2f31;
    --paper: #ffffff;
    --backdrop: #e6e6e6;
    --ink-white: #ffffff;
  }
  * { margin: 0; padding: 0; box-sizing: border-box; }
  html, body {
    width: 1040px; height: 1200px; overflow: hidden;
    background: var(--backdrop);
  }
  body { position: relative; font-family: "Archivo", Arial, sans-serif; }

  .poster {
    position: absolute; left: 140px; top: 30px;
    width: 760px; height: 1140px;
    background: var(--paper);
    overflow: hidden;
    box-shadow: 0 4px 14px rgba(0,0,0,0.18);
  }
  .poster__divider { position: absolute; left: 0; top: 0; width: 760px; height: 460px; }

  .brand {
    position: absolute; left: 318px; top: 110px;
    display: flex; align-items: center; gap: 14px;
  }
  .brand__square { width: 26px; height: 26px; background: var(--brand-blue); }
  .brand__name {
    font-weight: 800; font-stretch: 125%;
    font-size: 30px; letter-spacing: 1px;
    color: var(--brand-blue); line-height: 1;
    text-transform: uppercase;
  }

  .question {
    position: absolute; right: 76px; top: 285px;
    color: var(--ink-white); font-weight: 900; text-align: left;
    line-height: 1;
  }
  .question__lead { display: block; font-size: 47px; letter-spacing: 0.5px; }
  .question__main { display: block; font-size: 72px; margin-top: 18px; letter-spacing: 0.5px; }

  .purpose {
    position: absolute; left: 0; top: 463px; width: 760px; height: 528px;
    background: var(--charcoal);
  }
  .purpose__line {
    position: absolute; left: 0; width: 100%;
    text-align: center; font-weight: 900; line-height: 1;
    text-transform: uppercase; white-space: nowrap;
  }
  .purpose__line--white { color: var(--ink-white); }
  .purpose__line--blue { color: var(--brand-blue); }
  .l1 { top: 45px;  font-size: 47px; }
  .l2 { top: 116px; font-size: 44px; }
  .l3 { top: 167px; font-size: 62px; font-stretch: 110%; }
  .l4 { top: 255px; font-size: 36px; }
  .l5 { top: 310px; font-size: 48px; }
  .l6 { top: 370px; font-size: 56px; }
  .l7 { top: 423px; font-size: 78px; font-stretch: 105%; }

  .motto {
    position: absolute; left: 0; top: 991px; width: 760px; height: 149px;
    background: var(--brand-blue);
    display: flex; align-items: center; justify-content: center;
  }
  .motto__text {
    color: var(--ink-white); font-weight: 900; font-style: italic;
    font-size: 50px; letter-spacing: 0.5px; text-transform: uppercase;
  }
</style>
</head>
<body>
  <main class="poster">
    <svg class="poster__divider" viewBox="0 0 760 460" aria-hidden="true">
      <polygon points="0,188 173,270 253,233 760,233 760,460 0,460" fill="var(--brand-blue)"/>
      <polygon points="0,188 173,270 253,228 760,228 760,240 253,246 173,292 0,210" fill="var(--charcoal)"/>
    </svg>

    <div class="brand">
      <span class="brand__square"></span>
      <span class="brand__name">Larkmoor Property Management</span>
    </div>

    <h1 class="question">
      <span class="question__lead">WHY DO I COME</span>
      <span class="question__main">TO WORK?</span>
    </h1>

    <section class="purpose">
      <p class="purpose__line purpose__line--white l1">To feel fulfilled by</p>
      <p class="purpose__line purpose__line--blue l2">Empathizing, educating</p>
      <p class="purpose__line purpose__line--blue l3">and empowering</p>
      <p class="purpose__line purpose__line--white l4">our clients and co-workers</p>
      <p class="purpose__line purpose__line--white l5">so that we can build</p>
      <p class="purpose__line purpose__line--blue l6">strong, impactful</p>
      <p class="purpose__line purpose__line--blue l7">relationships</p>
    </section>

    <footer class="motto">
      <p class="motto__text">Own the outcome</p>
    </footer>
  </main>
</body>
</html>
```